KVT Roofing Pty Ltd

We are a high end residential Roofing company
We would like something silimar to the attached logo with the same color scheme

Target Market(s)

High end residential Builders & Architects

Industry/Entity Type

Residential

```html
<!DOCTYPE html>
<html lang="en">
<head>
<meta charset="UTF-8">
<title>R4 Roofworks – Business Card</title>
<link href="https://fonts.googleapis.com/css2?family=Arimo:wght@400;700&display=swap" rel="stylesheet">
<style>
  :root {
    --backdrop: #a9865c;
    --card: #ffffff;
    --card-edge: #8f8f8f;
    --slate: #3f4e59;
    --sky: #1d9fd3;
    --ink: #3a3a3a;
    --brand-light: #f2f2f2;
  }
  * { box-sizing: border-box; margin: 0; padding: 0; }
  html, body {
    width: 1100px; height: 1200px; overflow: hidden;
    background: var(--backdrop);
    font-family: "Arimo", Arial, sans-serif;
  }
  .canvas { position: relative; width: 1100px; height: 1200px; }
  .card {
    position: absolute; left: 138px; width: 821px; height: 470px;
    background: var(--card);
    border: 1px solid var(--card-edge);
    box-shadow: 0 2px 6px rgba(0,0,0,0.25);
  }
  .card-front { top: 81px; }
  .card-back { top: 624px; }

  .brand-block {
    position: absolute; left: 50%; top: 31px; transform: translateX(-50%);
    width: 232px; height: 191px; background: var(--slate);
  }
  .brand-name {
    position: absolute; left: 0; right: 0; top: 233px;
    text-align: center; font-weight: 700; font-size: 31px;
    letter-spacing: 1px; color: var(--slate);
  }
  .person {
    position: absolute; left: 0; right: 0; top: 302px;
    text-align: center; padding-left: 140px;
    color: var(--slate);
  }
  .person-name { font-weight: 700; font-size: 29px; }
  .person-role { font-size: 23px; color: var(--sky); margin-left: 4px; }
  .divider {
    position: absolute; left: 0; right: 0; top: 350px; height: 4px;
    background: linear-gradient(90deg, rgba(29,159,211,0) 0%, rgba(29,159,211,0.9) 50%, rgba(29,159,211,0) 100%);
  }
  .contact-row {
    position: absolute; left: 0; right: 0; top: 372px;
    display: flex; justify-content: center; align-items: center; gap: 22px;
    font-size: 21px; color: var(--ink);
  }
  .contact-item { display: flex; align-items: center; gap: 9px; }
  .contact-item svg { width: 18px; height: 18px; fill: var(--sky); }
  .address {
    position: absolute; left: 0; right: 0; top: 422px;
    text-align: center; font-size: 21px; color: var(--ink);
  }
  .brand-panel {
    position: absolute; left: 50%; top: 62px; transform: translateX(-50%);
    width: 401px; height: 333px; background: var(--slate);
    display: flex; align-items: center; justify-content: center;
  }
  .brand-panel-name {
    font-weight: 700; font-size: 40px; letter-spacing: 2px; color: var(--brand-light);
  }
</style>
</head>
<body>
<main class="canvas">
  <section class="card card-front">
    <div class="brand-block"></div>
    <div class="brand-name">R4 ROOFWORKS</div>
    <div class="person">
      <span class="person-name">Corin Ashby,</span><span class="person-role">General Manager</span>
    </div>
    <div class="divider"></div>
    <div class="contact-row">
      <span class="contact-item">
        <svg viewBox="0 0 24 24" aria-hidden="true"><path d="M6.6 10.8a15.1 15.1 0 0 0 6.6 6.6l2.2-2.2a1 1 0 0 1 1-.25 11.4 11.4 0 0 0 3.6.57 1 1 0 0 1 1 1V20a1 1 0 0 1-1 1A17 17 0 0 1 3 4a1 1 0 0 1 1-1h3.5a1 1 0 0 1 1 1c0 1.25.2 2.45.57 3.57a1 1 0 0 1-.25 1z"/></svg>
        0400 118 226
      </span>
      <span class="contact-item">
        <svg viewBox="0 0 24 24" aria-hidden="true"><path d="M2 6.5A1.5 1.5 0 0 1 3.5 5h17A1.5 1.5 0 0 1 22 6.5v.4l-10 6.2L2 6.9z"/><path d="M2 9.2l10 6.2 10-6.2v8.3a1.5 1.5 0 0 1-1.5 1.5h-17A1.5 1.5 0 0 1 2 17.5z"/></svg>
        cashby@harbourlineroofing.com.au
      </span>
    </div>
    <div class="address">27 Wattle Lane, Port Melbourne</div>
  </section>

  <section class="card card-back">
    <div class="brand-panel">
      <span class="brand-panel-name">R4 ROOFWORKS</span>
    </div>
  </section>
</main>
</body>
</html>
```